Design some Business Cards for an existing business

Logo is attached, please submit entries

Please set out contact details in following format

Name :
Job Title:
email
phone:
address

Business is a health supplement business catering to fitness enthusiasts

```html
<!DOCTYPE html>
<html lang="en">
<head>
<meta charset="utf-8">
<title>Ironvale Nutrition – Business Cards</title>
<link href="https://fonts.googleapis.com/css2?family=Oswald:wght@500&family=Open+Sans:wght@400;600&display=swap" rel="stylesheet">
<style>
  :root {
    --page: #e9e7e4;
    --card: #141414;
    --card-edge: #1c1c1c;
    --panel: #1e1e1e;
    --rule: #3a3a3a;
    --ink: #f2f2f2;
    --ink-soft: #bdbdbd;
    --ink-muted: #8c8c8c;
  }
  * { box-sizing: border-box; margin: 0; padding: 0; }
  html, body { width: 1200px; height: 889px; overflow: hidden; }
  body {
    background: var(--page);
    font-family: "Open Sans", sans-serif;
    color: var(--ink);
    display: flex;
    align-items: center;
    justify-content: center;
    gap: 40px;
  }
  .card {
    width: 540px;
    height: 309px;
    background: linear-gradient(160deg, var(--card-edge), var(--card));
    border-radius: 4px;
    box-shadow: 0 10px 24px rgba(0,0,0,.25);
    position: relative;
    overflow: hidden;
  }
  .brand {
    display: flex;
    align-items: center;
    gap: 12px;
    font-family: "Oswald", sans-serif;
    font-weight: 500;
    color: var(--ink);
    text-transform: uppercase;
    letter-spacing: 2px;
  }
  .brand-dot {
    width: 22px; height: 22px;
    border-radius: 50%;
    background: var(--ink);
    flex: none;
  }
  /* front */
  .card-front {
    display: flex;
    flex-direction: column;
    align-items: center;
    justify-content: center;
    gap: 22px;
  }
  .card-front .brand { font-size: 30px; }
  .web-line {
    display: flex;
    align-items: center;
    gap: 12px;
    font-size: 12px;
    color: var(--ink-soft);
    letter-spacing: .5px;
  }
  .web-line::before, .web-line::after {
    content: "";
    width: 30px; height: 1px;
    background: var(--ink-muted);
  }
  /* back */
  .card-back .brand {
    position: absolute;
    left: 30px; top: 128px;
    font-size: 19px;
    gap: 10px;
  }
  .card-back .brand-dot { width: 16px; height: 16px; }
  .contact-panel {
    position: absolute;
    right: 0; top: 0; bottom: 0;
    width: 270px;
    background: var(--panel);
    padding: 34px 22px 0 26px;
  }
  .person { text-align: right; margin-bottom: 14px; }
  .person-name { font-size: 17px; font-weight: 600; }
  .person-title { font-size: 11px; color: var(--ink-soft); }
  .contact-list { list-style: none; }
  .contact-item {
    display: flex;
    align-items: flex-start;
    gap: 10px;
    font-size: 12.5px;
    line-height: 1.35;
    color: var(--ink);
    padding: 10px 0;
    border-top: 1px solid var(--rule);
  }
  .contact-item:last-child { border-bottom: 1px solid var(--rule); }
  .contact-icon { width: 15px; height: 15px; flex: none; margin-top: 1px; }
</style>
</head>
<body>
  <section class="card card-front">
    <div class="brand"><span class="brand-dot"></span>Ironvale Nutrition</div>
    <div class="web-line">www.ironvalenutrition.com</div>
  </section>

  <section class="card card-back">
    <div class="brand"><span class="brand-dot"></span>Ironvale Nutrition</div>
    <div class="contact-panel">
      <div class="person">
        <div class="person-name">Daniel Harper</div>
        <div class="person-title">Managing Director</div>
      </div>
      <ul class="contact-list">
        <li class="contact-item">
          <svg class="contact-icon" viewBox="0 0 16 16" fill="none" stroke="#f2f2f2" stroke-width="1.4"><rect x="4" y="1" width="8" height="14" rx="1.5"/><line x1="7" y1="12.5" x2="9" y2="12.5"/></svg>
          <span>+ 1 (555) 014 2287</span>
        </li>
        <li class="contact-item">
          <svg class="contact-icon" viewBox="0 0 16 16" fill="none" stroke="#f2f2f2" stroke-width="1.4"><rect x="1.5" y="3.5" width="13" height="9" rx="1"/><polyline points="1.5,4 8,9 14.5,4"/></svg>
          <span>daniel.harper@ironvale</span>
        </li>
        <li class="contact-item">
          <svg class="contact-icon" viewBox="0 0 16 16" fill="none" stroke="#f2f2f2" stroke-width="1.4"><path d="M8 15s5-5 5-8.5A5 5 0 0 0 3 6.5C3 10 8 15 8 15z"/><circle cx="8" cy="6.5" r="1.8"/></svg>
          <span>1820 Foundry Road<br>Harrisburg, PA 17110</span>
        </li>
      </ul>
    </div>
  </section>
</body>
</html>
```